"Web Design" E-commerce web site * give me the BEST Equipment website

We require an
Truely EYE catching E-COMMERCE website “Fusion Supply Australia”
Branded as FSA

**** ARE YOU UP TO THE CHALLENGE !!!! ***

We already have 2 website names registered :
www.fusegoods.com.au and www.fusionsupplyaustralia.com.au
( one is active but unfinished)

If you need to see what will APPEAL TO ME "The two websites below have a lot of what I am looking for (design Style ) www.quorvatech.com & www.zelthemes.com/live/?theme=marivanta
Therefore -a combination of these two sites best features would be very close. !
please use and index with similar catergories to: www.fusionsupplyaustralia.com.au

CONCEPT OF SITE
Customer places order through transaction system.. -all payment methods
 which immediately send order through to my own staff and or the respective supplier. (Option for site administrator to choose for each product listing who receives such email)
 Product listings must be easily edited / updated and or replaced by personell with limited computer knowledge (if they can use chatterbook or yourplace they should be able to edit product listings) simply put they will need NO CODE EDITING SKILLS REQUIRED.

Please create a pages for atleast the following:
Main home page
 Brantor products only
 Torvalk products only
 Ossari products only
 Fusequeen products only
 Electrical supplies
 Power Distribution
 Mine spec’d equipment specials
2nd hand equipment
contact
about us
sitemap

Information to populate fields with in pages can be source from our suppliers own websites as we are authorised distributors of the following sites:

http://www.brantorpower.com.au/catalogue/page3/category1
http://www.torvalk.com.au/product-category/welding-machines/
http://www.fusequeen.com.au/products/
http://www.ossari.com

concept:
Basically, the website is to be for the fast movement of stock from Our own stock and Our suppliers – direct to the customers address (drop shipping) with very LIMITED INTERACTION with our customers (email only)
Updates

           SEE IMAGES IN ATTACHED RAR    

ALSO CHECK OUT THESE SITES WHICH SHOW THE STYLES I LIKE  SO THEY WILL HELP YOU DESIGN SOMETHING THAT GETS CLOSER TO MY IDEAL SITE AND MY REQUIREMENTS

we are currently running a poll and will make a decision very shortly.. thanks to all

Target Market(s)

Males 20 to 55
engineering and handyman

Industry/Entity Type

Computer

Requirements
Must have
• That wow factor.. grabs your attention not through tacky.. but well designed / layout
Ease of editing / updating

shipping and freight calculator that automatically adds to invioce

NON compulsory Newsletter - although if customers provide validation of email they receive 2.5% discount on purchases (enter a code sent to them)

the rest is just simple.. amaze me with your talents
Nice to have
• Todays quick sales - campaign
Weekly quick sales - campaign

highlight specials

```html
<!DOCTYPE html>
<html lang="en">
<head>
<meta charset="utf-8">
<title>Fusion Supply Australia</title>
<link rel="stylesheet" href="https://fonts.googleapis.com/css2?family=Open+Sans:wght@700;800&family=Questrial&family=Tinos:wght@400;700&display=swap">
<style>
:root{
  --ink:#333333;
  --black:#000000;
  --header-top:#5a5a5a;
  --header-bottom:#2e2e2e;
  --nav-bg:#ececec;
  --accent:#d86a0c;
  --accent-bright:#f29311;
  --hero-bg:#d9d9d9;
  --panel-line:#c9c9c9;
  --page:#f2f2f2;
  --muted:#555555;
  --white:#ffffff;
  --dark-band:#333333;
}
*{box-sizing:border-box;margin:0;padding:0}
html,body{width:1000px;height:1200px;overflow:hidden}
body{position:relative;background:linear-gradient(#ececec,#fafafa 60%,#ffffff);font-family:"Questrial",Arial,sans-serif;color:var(--ink)}
.abs{position:absolute}

.utility-bar{left:0;top:0;width:1000px;height:36px;background:var(--black)}
.utility-bar a{position:absolute;top:11px;font-family:"Tinos",serif;font-size:13px;color:#cfcfcf;text-decoration:none}

.site-header{left:0;top:36px;width:1000px;height:109px;background:linear-gradient(var(--header-top),var(--header-bottom))}
.brand{left:56px;top:36px;color:#d6d6d6}
.brand-name{font-family:"Open Sans",sans-serif;font-weight:800;font-size:30px;letter-spacing:.5px;line-height:30px}
.brand-tag{font-family:"Questrial",sans-serif;font-size:14px;letter-spacing:.6px;margin-left:3px;line-height:16px}
.cart{left:731px;top:6px;width:220px;height:40px;border:1px solid #6a6a6a;background:#2b2b2b}
.cart-icon{position:absolute;left:0;top:0;width:43px;height:38px;border-right:1px solid #6a6a6a;display:flex;align-items:center;justify-content:center}
.cart-label{position:absolute;left:54px;top:11px;font-family:"Tinos",serif;font-size:13px;color:#e5e5e5;white-space:nowrap}
.cart-label b{color:var(--accent-bright);font-size:14px;margin-right:6px}
.search{left:731px;top:53px;width:221px;height:41px}
.search-field{position:absolute;left:0;top:0;width:174px;height:41px;background:#2c2c2c;border:1px solid #676767}
.search-btn{position:absolute;left:173px;top:0;width:48px;height:41px;background:linear-gradient(#f6a21a,#e07c08);border-radius:0 3px 3px 0;display:flex;align-items:center;justify-content:center}

.main-nav{left:0;top:145px;width:1000px;height:67px;background:var(--nav-bg);border-bottom:1px solid #d8d8d8}
.home-tab{left:50px;top:0;width:63px;height:67px;background:linear-gradient(#4e4e4e,#2f2f2f);display:flex;align-items:center;justify-content:center}
.main-nav a{position:absolute;top:24px;font-size:18px;color:var(--ink);text-decoration:none;letter-spacing:.2px}

.hero{left:0;top:217px;width:1000px;height:384px;background:var(--hero-bg)}
.hero-title{left:50px;top:59px;font-family:"Open Sans",sans-serif;font-weight:800;font-size:58px;letter-spacing:1px;color:#333;line-height:64px}
.hero-sub{left:51px;top:124px;font-size:31px;color:#555;letter-spacing:.6px}
.shop-btn{left:50px;top:245px;width:153px;height:58px;background:var(--dark-band);color:var(--accent);font-size:20px;display:flex;align-items:center;justify-content:center}
.dot{top:341px;width:15px;height:15px;border-radius:50%;background:#666}
.dot.active{background:var(--accent)}
.hero-image{left:592px;top:47px;width:244px;height:290px;background:linear-gradient(135deg,#c23a2e,#8f2019 60%,#2a2a2a);border-radius:6px}

.featured{top:627px;width:282px;height:124px;background:linear-gradient(#ffffff,#e9e9e9);border:1px solid #bdbdbd;overflow:hidden}
.featured-image{position:absolute;left:34px;top:12px;width:94px;height:70px;background:linear-gradient(#3c6fb8,#2b4f8a 65%,#2a2a2a);border-radius:3px}
.featured-price{position:absolute;left:151px;top:28px;font-size:21px;color:var(--accent)}
.featured-text{position:absolute;left:151px;top:55px;font-size:12.5px;line-height:16px;color:#555;width:118px;letter-spacing:.3px}
.featured-ribbon{position:absolute;right:-30px;top:18px;width:140px;height:20px;background:var(--accent);color:#fff;font-size:11px;text-align:center;line-height:20px;transform:rotate(38deg)}
.featured-band{position:absolute;left:0;bottom:0;width:100%;height:28px;background:var(--dark-band);color:var(--accent);font-size:15px;text-align:right;padding:5px 20px 0 0}

.section-head{left:50px;top:805px;width:881px;height:49px;background:linear-gradient(#ffffff,#ebebeb);border:1px solid #cfcfcf;padding:15px 0 0 17px;font-size:16px;color:#555;letter-spacing:.3px}

.product{top:870px;width:190px;height:160px}
.product-image{position:absolute;left:28px;top:4px;width:97px;height:116px;background:linear-gradient(135deg,#c9392b,#8e1e17 55%,#232323);border-radius:4px}
.product-price{position:absolute;left:142px;top:84px;font-size:20px;color:var(--accent)}
.product-name{position:absolute;left:29px;top:143px;font-family:"Open Sans",sans-serif;font-weight:700;font-size:12.5px;color:#222}
.detail-btn{position:absolute;left:149px;top:130px;width:55px;height:27px;border:1px solid #bbb;border-radius:4px;background:linear-gradient(#fdfdfd,#dcdcdc);font-size:12px;color:#444;text-align:center;line-height:26px}

.site-footer{left:50px;top:1037px;width:881px;height:127px;background:linear-gradient(#f7f7f7,#ebebeb);border:1px solid #cfcfcf}
.footer-bar{position:absolute;left:0;top:0;width:100%;height:31px;background:linear-gradient(#ffffff,#e3e3e3);border-bottom:1px solid #d6d6d6}
.footer-heading{position:absolute;top:10px;font-size:12px;color:#222;letter-spacing:.2px}
.footer-list{position:absolute;list-style:none;font-size:10px;color:#333;line-height:19.3px;letter-spacing:.3px}
.newsletter-field{position:absolute;left:688px;top:70px;width:169px;height:31px;border:1px solid #c4c4c4;border-radius:3px 0 0 3px;background:#fff}
.newsletter-btn{position:absolute;left:822px;top:70px;width:35px;height:31px;border:1px solid #c4c4c4;border-radius:0 3px 3px 0;background:linear-gradient(#fdfdfd,#e2e2e2);display:flex;align-items:center;justify-content:center}
</style>
</head>
<body>

<nav class="utility-bar abs">
  <a href="#" style="left:55px">Check out</a>
  <a href="#" style="left:161px">Wish List</a>
  <a href="#" style="left:263px">LogIn</a>
</nav>

<header class="site-header abs">
  <div class="brand abs">
    <div class="brand-name">FUSION SUPPLY</div>
    <div class="brand-tag">BEST CHOICE IN AUSTRALIA</div>
  </div>
  <div class="cart abs">
    <div class="cart-icon">
      <svg width="26" height="22" viewBox="0 0 26 22" fill="none" stroke="#e8e8e8" stroke-width="1.6">
        <path d="M1 2h4l3 12h13l3-9H7"/><circle cx="10" cy="18.5" r="1.8"/><circle cx="19" cy="18.5" r="1.8"/>
        <path d="M9 8h14M10 11h12" stroke-width="1"/>
      </svg>
    </div>
    <div class="cart-label"><b>Cart:</b>0 items - AUD 0
      <svg width="9" height="7" viewBox="0 0 9 7" style="margin-left:6px"><path d="M1 1l3.5 4L8 1" stroke="#fff" stroke-width="1.8" fill="none"/></svg>
    </div>
  </div>
  <div class="search abs">
    <div class="search-field"></div>
    <div class="search-btn">
      <svg width="28" height="24" viewBox="0 0 28 24"><circle cx="10" cy="9" r="6.5" fill="none" stroke="#fff" stroke-width="3"/><path d="M15 13l9 8" stroke="#fff" stroke-width="4" stroke-linecap="round"/></svg>
    </div>
  </div>
</header>

<nav class="main-nav abs">
  <div class="home-tab abs">
    <svg width="24" height="20" viewBox="0 0 24 20"><path d="M12 1L1 11h3v8h6v-5h4v5h6v-8h3z" fill="#e07a10"/></svg>
  </div>
  <a href="#" style="left:177px">PRODUCTS</a>
  <a href="#" style="left:338px">2nd HAND EQUIPMENT</a>
  <a href="#" style="left:615px">ABOUT US</a>
  <a href="#" style="left:781px">CONTACT</a>
</nav>

<section class="hero abs">
  <h1 class="hero-title abs">BEST EQUIPMENT</h1>
  <p class="hero-sub abs">Lorem ipsum dolor sit amet</p>
  <div class="shop-btn abs">SHOP NOW</div>
  <span class="dot abs" style="left:50px"></span>
  <span class="dot active abs" style="left:80px"></span>
  <span class="dot abs" style="left:112px"></span>
  <div class="hero-image abs" role="img" aria-label="Red engine-driven welding machine"></div>
</section>

<article class="featured abs" style="left:49px">
  <div class="featured-image" role="img" aria-label="Blue portable welder generator"></div>
  <div class="featured-price">88 AUD</div>
  <div class="featured-text">Lorem ipsum dolor sit amet</div>
  <div class="featured-ribbon">FEATURED</div>
  <div class="featured-band">SHOP NOW</div>
</article>
<article class="featured abs" style="left:350px">
  <div class="featured-image" role="img" aria-label="Blue portable welder generator"></div>
  <div class="featured-price">88 AUD</div>
  <div class="featured-text">Lorem ipsum dolor sit amet</div>
  <div class="featured-ribbon">FEATURED</div>
  <div class="featured-band">SHOP NOW</div>
</article>
<article class="featured abs" style="left:649px">
  <div class="featured-image" role="img" aria-label="Blue portable welder generator"></div>
  <div class="featured-price">88 AUD</div>
  <div class="featured-text">Lorem ipsum dolor sit amet</div>
  <div class="featured-ribbon">FEATURED</div>
  <div class="featured-band">SHOP NOW</div>
</article>

<h2 class="section-head abs" style="font-weight:400">NEW PRODUCTS</h2>

<article class="product abs" style="left:50px">
  <div class="product-image" role="img" aria-label="Red welding machine"></div>
  <div class="product-price">88 AUD</div>
  <div class="product-name">Lorem ipsum</div>
  <div class="detail-btn">DETAIL</div>
</article>
<article class="product abs" style="left:275px">
  <div class="product-image" role="img" aria-label="Red welding machine"></div>
  <div class="product-price">88 AUD</div>
  <div class="product-name">Lorem ipsum</div>
  <div class="detail-btn" style="left:147px">DETAIL</div>
</article>
<article class="product abs" style="left:502px">
  <div class="product-image" role="img" aria-label="Red welding machine"></div>
  <div class="product-price">88 AUD</div>
  <div class="product-name">Lorem ipsum</div>
  <div class="detail-btn" style="left:148px">DETAIL</div>
</article>
<article class="product abs" style="left:726px">
  <div class="product-image" role="img" aria-label="Red welding machine"></div>
  <div class="product-price">88 AUD</div>
  <div class="product-name">Lorem ipsum</div>
  <div class="detail-btn" style="left:146px">DETAIL</div>
</article>

<footer class="site-footer abs">
  <div class="footer-bar"></div>
  <div class="footer-heading" style="left:21px">INFORMATION</div>
  <div class="footer-heading" style="left:465px">MY ACCOUNT</div>
  <div class="footer-heading" style="left:687px">NEWSLETTER</div>
  <ul class="footer-list" style="left:17px;top:37px">
    <li>Shipping &amp;Return</li><li>Privacy Policy</li><li>Condition of use</li><li>Site Map</li>
  </ul>
  <ul class="footer-list" style="left:244px;top:55px">
    <li>Contact Us</li><li>Discount Coupons</li><li>Gift Certificates FAQ</li>
  </ul>
  <ul class="footer-list" style="left:464px;top:37px">
    <li>Sign In</li><li>View Cart</li><li>My Wishlist</li><li>Track my order</li>
  </ul>
  <ul class="footer-list" style="left:688px;top:38px"><li>Sign In for our newsletter</li></ul>
  <div class="newsletter-field"></div>
  <div class="newsletter-btn">
    <svg width="7" height="10" viewBox="0 0 7 10"><path d="M1.5 1l4 4-4 4" stroke="#222" stroke-width="2" fill="none"/></svg>
  </div>
</footer>

</body>
</html>
```